Build a Web page - Dorin Vaughtley Homes, LLC - a custom home builder

We are a custom home builder in Wisconsin. Need a basic web page with a home page, About Us, Contact info, Gallery, and Testimonials page. Gallery will probably have sub-pages and each will have about ten pictures or less. I already own the domain and have web hosting through Wix, I just need the site built. Once the page is built I should be able to do the upkeep on it myself. If I need to add pictures or whatever.
Updates

Project Deadline Extended
Reason: I am still looking through designs and will select soon - thank you!

Target Market(s)

Gen X and Millennials who are looking to build a home. Custom built homes - not generic spec homes.

Industry/Entity Type

Home Builder

Number of Pages Required

5+ page

Font styles to use
Sans Serif

Colors
ffffff
ec1f27
000000
9d9d9d

Requirements
Must have
• I have no idea if I want coded or in coded. I'm not sure of the difference and why I would want one over the other.
Nice to have
• We like the following colors - red, black, gray, white.
Should not have
• not a big fan of clip art like hammers, tape measures, etc. Must look professional.

```html
<!DOCTYPE html>
<html lang="en">
<head>
<meta charset="utf-8">
<title>Dorin Vaughtley Homes, LLC</title>
<link href="https://fonts.googleapis.com/css2?family=Open+Sans:ital,wght@0,400;0,600;0,700;0,800;1,400&display=swap" rel="stylesheet">
<style>
:root{
  --red:#ec1f27;
  --black:#000000;
  --white:#ffffff;
  --grey:#9d9d9d;
  --text:#555555;
  --ink:#111111;
  --band:#f4f4f4;
  --frame:#e3e3e3;
}
*{margin:0;padding:0;box-sizing:border-box}
html,body{width:1200px;height:2503px;overflow:hidden}
body{font-family:"Open Sans",sans-serif;background:var(--white);color:var(--text);position:relative}
.abs{position:absolute}
.topline{left:0;top:0;width:1200px;height:5px;background:var(--black)}
.brand{left:75px;top:20px;height:80px;display:flex;align-items:center;gap:10px}
.brand .mark{width:22px;height:22px;background:var(--red)}
.brand .name{font-size:17px;font-weight:700;color:var(--ink);line-height:1.15;width:130px}
.phone{left:938px;top:5px;width:189px;height:40px;background:var(--black);color:var(--white);font-size:20px;display:flex;align-items:center;justify-content:center;gap:12px}
.nav{top:75px;font-size:14px;font-weight:700;color:var(--ink);letter-spacing:.3px}
.nav.active{color:var(--red)}
.hero{left:0;top:110px;width:1200px;height:546px;background:linear-gradient(180deg,#6f95d6 0%,#b9cde6 30%,#6f7a5e 48%,#5f8a3a 62%,#4e8a2a 100%)}
.hero h1{position:absolute;left:0;top:212px;width:1200px;text-align:center;color:var(--white);font-size:36px;font-weight:800;line-height:43px;text-shadow:0 2px 4px rgba(0,0,0,.5)}
.btn-solid{left:524px;top:436px;width:152px;height:45px;background:var(--red);color:var(--white);font-size:14px;font-weight:700;display:flex;align-items:center;justify-content:center}
.dot{top:620px;width:11px;height:11px;border-radius:50%;background:var(--white)}
.dot.on{background:var(--red)}
.h2{font-size:23px;font-weight:700;color:var(--ink);letter-spacing:.4px}
.h2 span{color:var(--red)}
.body{font-size:14.5px;line-height:24px;color:var(--text)}
.btn-line{width:150px;height:45px;border:2px solid var(--red);color:var(--red);font-size:14px;font-weight:700;display:flex;align-items:center;justify-content:center}
.frame{border:6px solid var(--frame);background:var(--white);padding:12px}
.frame div{width:100%;height:100%}
.band{left:0;width:1200px;background:var(--band)}
.grid{left:75px;top:1475px;width:1052px;height:411px}
.tile{position:absolute}
.center{left:0;width:1200px;text-align:center}
.avatar{width:90px;height:88px;background:linear-gradient(180deg,#d9d4cf,#b9aea4)}
.quote{width:215px;font-size:14.5px;line-height:24px;font-style:italic;color:var(--text)}
.sig{font-size:13px;font-weight:700;color:var(--red)}
.footer{left:0;top:2256px;width:1200px;height:247px;background:var(--black)}
.fhead{font-size:14px;font-weight:700;color:var(--white);letter-spacing:.4px}
.flink{font-size:12.5px;color:#dddddd}
.input{left:885px;top:2327px;width:195px;height:40px;background:var(--white);font-size:12.5px;color:#555;display:flex;align-items:center;padding-left:14px}
.send{left:1080px;top:2327px;width:47px;height:40px;background:var(--red);display:flex;align-items:center;justify-content:center}
.social{top:2430px;width:24px;height:24px;border-radius:50%;background:#8a8a8a}
</style>
</head>
<body>
<div class="abs topline"></div>

<header>
  <div class="abs brand"><div class="mark"></div><div class="name">Dorin Vaughtley Homes</div></div>
  <div class="abs phone">
    <svg width="16" height="16" viewBox="0 0 24 24"><path fill="#fff" d="M6.6 10.8a15 15 0 0 0 6.6 6.6l2.2-2.2c.3-.3.7-.4 1-.2 1.1.4 2.3.6 3.6.6.6 0 1 .4 1 1V20c0 .6-.4 1-1 1A17 17 0 0 1 3 4c0-.6.4-1 1-1h3.5c.6 0 1 .4 1 1 0 1.3.2 2.5.6 3.6.1.3 0 .7-.2 1z"/></svg>
    <span>920-555-0142</span>
  </div>
  <nav>
    <a class="abs nav active" style="left:576px">HOME</a>
    <a class="abs nav" style="left:664px">ABOUT US</a>
    <a class="abs nav" style="left:779px">GALLERY</a>
    <a class="abs nav" style="left:886px">TESTIMONIALS</a>
    <a class="abs nav" style="left:1035px">CONTACT US</a>
  </nav>
</header>

<section class="abs hero" role="img" aria-label="Two-storey green-sided family home on a wide lawn under a blue sky">
  <h1>VESTIBULUM ANTE IPSUM PRIMIS<br>IN FAUCIBUS ULTRICES</h1>
  <div class="abs btn-solid">READ MORE</div>
  <div class="abs dot on" style="left:568px"></div>
  <div class="abs dot" style="left:584px"></div>
  <div class="abs dot" style="left:600px"></div>
  <div class="abs dot" style="left:616px"></div>
</section>

<section class="welcome">
  <h2 class="abs h2" style="left:75px;top:712px">WELCOME TO <span>DORIN VAUGHTLEY HOMES, LLC</span></h2>
  <p class="abs body" style="left:75px;top:759px;width:695px">Aliquam molestie, mi et imperdiet euismod, dui purus auctor tellus, et interdum lacus lectus et ante. Sed accumsan sollicitudin sapien, sit amet adipiscing turpis gravida ac. In congue, neque ac lobortis volutpat, libero mauris varius mi, vitae suscipit ipsum ligula vitae risus. Duis aliquam nibh a dui iaculis viverra id a velit. Vivamus egestas risus in magna varius commodo. Sed semper viverra egestas. Etiam pretium porttitor lectus, vel ornare neque porta volutpat.</p>
  <div class="abs btn-line" style="left:75px;top:908px">READ MORE</div>
  <div class="abs frame" style="left:795px;top:703px;width:332px;height:268px">
    <div role="img" aria-label="Green two-storey custom home with attached garage and front lawn" style="background:linear-gradient(180deg,#5f92d8 0%,#a9c4e4 35%,#5d6a52 55%,#4f8a2c 100%)"></div>
  </div>
</section>

<section class="abs band" style="top:1018px;height:367px"></section>
<section class="builder">
  <div class="abs frame" style="left:75px;top:1068px;width:330px;height:269px">
    <div role="img" aria-label="Back of a beige ranch home with a stone patio and outdoor dining set" style="background:linear-gradient(180deg,#e9ecef 0%,#d8d2c6 40%,#a79a85 65%,#4f8a2c 100%)"></div>
  </div>
  <h2 class="abs h2" style="left:437px;top:1074px">WE ARE A <span>CUSTOM HOME BUILDER</span></h2>
  <p class="abs body" style="left:437px;top:1121px;width:695px">Aliquam molestie, mi et imperdiet euismod, dui purus auctor tellus, et interdum lacus lectus et ante. Sed accumsan sollicitudin sapien, sit amet adipiscing turpis gravida ac. In congue, neque ac lobortis volutpat, libero mauris varius mi, vitae suscipit ipsum ligula vitae risus. Duis aliquam nibh a dui iaculis viverra id a velit. Vivamus egestas risus in magna varius commodo. Sed semper viverra egestas. Etiam pretium porttitor lectus, vel ornare neque porta volutpat.</p>
  <div class="abs btn-line" style="left:437px;top:1270px">READ MORE</div>
</section>

<section class="gallery">
  <h2 class="abs h2 center" style="top:1418px">OUR <span>GALLERY</span></h2>
  <div class="abs grid">
    <div class="tile" role="img" aria-label="Bathroom with vanity and mirror" style="left:0;top:0;width:255px;height:162px;background:linear-gradient(135deg,#c9c48a,#a88a55)"></div>
    <div class="tile" role="img" aria-label="Dining and living room interior" style="left:0;top:165px;width:255px;height:246px;background:linear-gradient(135deg,#9a9a9c,#5a4840)"></div>
    <div class="tile" role="img" aria-label="Built-in wooden mudroom lockers" style="left:259px;top:0;width:253px;height:244px;background:linear-gradient(135deg,#b07a48,#7a4a26)"></div>
    <div class="tile" role="img" aria-label="Kitchen with wood cabinets and island" style="left:259px;top:247px;width:253px;height:164px;background:linear-gradient(135deg,#8a6a50,#4a3428)"></div>
    <div class="tile" role="img" aria-label="Bedroom with dark wood furniture and patterned quilt" style="left:516px;top:0;width:536px;height:244px;background:linear-gradient(135deg,#d7ccbd,#8a3a30 60%,#4a2e22)"></div>
    <div class="tile" role="img" aria-label="Rear wooden deck with patio furniture" style="left:516px;top:247px;width:265px;height:164px;background:linear-gradient(180deg,#d8d4c8,#8a4a3c 70%,#5a7a3a)"></div>
    <div class="tile" role="img" aria-label="Wooden staircase in a bright hallway" style="left:784px;top:247px;width:268px;height:164px;background:linear-gradient(135deg,#e2dccd,#8a4a2a)"></div>
  </div>
</section>

<section class="abs band" style="top:1936px;height:320px"></section>
<section class="testimonials">
  <h2 class="abs h2 center" style="top:1975px">OUR <span>TESTIMONIALS</span></h2>

  <div class="abs avatar" style="left:75px;top:2038px" role="img" aria-label="Client portrait"></div>
  <p class="abs quote" style="left:179px;top:2032px">“ Aliquam molestie, mi et imperdiet euismod, dui purus auctor tellus, et interdum lacus lectus et ante. Sed accumsan sollicitudin sapien, sit amet adipiscing turpiss..”</p>
  <p class="abs sig" style="left:179px;top:2193px">-NAME HEADING</p>

  <div class="abs avatar" style="left:436px;top:2038px" role="img" aria-label="Client portrait"></div>
  <p class="abs quote" style="left:540px;top:2032px">“ Aliquam molestie, mi et imperdiet euismod, dui purus auctor tellus, et interdum lacus lectus et ante. Sed accumsan sollicitudin sapien, sit amet adipiscing turpiss..”</p>
  <p class="abs sig" style="left:540px;top:2193px">-NAME HEADING</p>

  <div class="abs avatar" style="left:796px;top:2038px" role="img" aria-label="Client portrait"></div>
  <p class="abs quote" style="left:900px;top:2032px">“ Aliquam molestie, mi et imperdiet euismod, dui purus auctor tellus, et interdum lacus lectus et ante. Sed accumsan sollicitudin sapien, sit amet adipiscing turpiss..”</p>
  <p class="abs sig" style="left:900px;top:2193px">-NAME HEADING</p>
</section>

<footer class="abs footer">
  <div class="abs" style="left:75px;top:40px;display:flex;align-items:center;gap:8px">
    <div style="width:16px;height:16px;background:var(--red)"></div>
    <div style="font-size:14px;font-weight:700;color:var(--white);width:110px;line-height:1.2">Dorin Vaughtley Homes</div>
  </div>
  <p class="abs flink" style="left:75px;top:121px;font-size:11px;line-height:20px">Copyright © 2017. Company Name<br>All Right Reserved</p>

  <h3 class="abs fhead" style="left:352px;top:38px">SITE MAP</h3>
  <p class="abs flink" style="left:352px;top:68px">Home</p>
  <p class="abs flink" style="left:352px;top:96px">About us</p>
  <p class="abs flink" style="left:352px;top:124px">Gallery</p>
  <p class="abs flink" style="left:352px;top:152px">Testimonials</p>
  <p class="abs flink" style="left:352px;top:180px">Contact us</p>

  <h3 class="abs fhead" style="left:571px;top:38px">CONTACT INFO</h3>
  <p class="abs flink" style="left:571px;top:68px;line-height:21px">2417 Calder Lane,<br>Larkfield, WI 54021</p>
  <svg class="abs" style="left:571px;top:124px" width="12" height="12" viewBox="0 0 24 24"><path fill="#ddd" d="M6.6 10.8a15 15 0 0 0 6.6 6.6l2.2-2.2c.3-.3.7-.4 1-.2 1.1.4 2.3.6 3.6.6.6 0 1 .4 1 1V20c0 .6-.4 1-1 1A17 17 0 0 1 3 4c0-.6.4-1 1-1h3.5c.6 0 1 .4 1 1 0 1.3.2 2.5.6 3.6.1.3 0 .7-.2 1z"/></svg>
  <p class="abs flink" style="left:604px;top:120px">1-800-555-0199</p>
  <svg class="abs" style="left:571px;top:153px" width="13" height="10" viewBox="0 0 26 20"><rect width="26" height="20" fill="#ddd"/><path d="M0 0l13 10L26 0" stroke="#000" stroke-width="2" fill="none"/></svg>
  <p class="abs flink" style="left:604px;top:148px">info@dorinvaughtley.com</p>
  <svg class="abs" style="left:571px;top:179px" width="10" height="14" viewBox="0 0 20 28"><path fill="#ddd" d="M10 0a10 10 0 0 0-10 10c0 7 10 18 10 18s10-11 10-18A10 10 0 0 0 10 0zm0 14a4 4 0 1 1 0-8 4 4 0 0 1 0 8z"/></svg>
  <p class="abs flink" style="left:604px;top:177px">Map Location</p>

  <h3 class="abs fhead" style="left:885px;top:38px">EMAIL SIGN UP</h3>
  <div class="abs input" style="top:71px">Enter Email Address</div>
  <div class="abs send" style="top:71px"><svg width="14" height="20" viewBox="0 0 14 20"><path d="M3 2l8 8-8 8" stroke="#fff" stroke-width="3" fill="none"/></svg></div>
  <h3 class="abs fhead" style="left:885px;top:136px">FOLLOW US</h3>
  <div class="abs social" style="left:882px;top:174px"></div>
  <div class="abs social" style="left:920px;top:174px"></div>
  <div class="abs social" style="left:963px;top:174px"></div>
  <div class="abs social" style="left:1011px;top:174px"></div>
  <div class="abs social" style="left:1055px;top:174px"></div>
</footer>
</body>
</html>
```